Visitenkarten-Design für Lichtfeder - Zeilen von Hand zu Hand
Zielgruppe
Ich schreibe Briefe an Menschen, die mehr über sich erfahren wollen, die sich berühren lassen wollen, die an sich arbeiten möchten, die sich entfalten wollen. Ich möchte nicht den Verstand sondern das Herz ansprechen, die Selbstheilung erfahren möchten, damit sie Impulse bekommen, um ein glücklicheres Leben zu führen, das ihnen mehr entspricht.
Ich sehe mich als Mensch, der andere Menschen in ihrem Leben unterstützen möchte.
Aufgabenstellung
Die Briefe schreibe ich in Segoe Print, goldene Schrift auf gelblichem Papier, evtl auch anderes Papier, wenn die goldene Schrift passt.
Die Visitenkarte sollte Freude, Freiheit und Anerkennung des Menschen an sich ausstrahlen. Farben evtl. Bordeaux, mit vielleicht Rosa. Sie sollte jedoch nicht kitschig wirken.
Schön wäre vielleicht etwas mit Blumen oder Ornamenten, jedoch nicht zu überladen.
Als Text soll drauf sein:
Das beigefügte Logo, dann:
Berühren - Bewegen - Begeistern

```html
<!DOCTYPE html>
<html lang="de">
<head>
<meta charset="utf-8">
<title>Lichtfeder – Visitenkarte</title>
<link rel="stylesheet" href="https://fonts.googleapis.com/css2?family=Playball&family=Raleway:wght@500;600&display=swap">
<style>
  :root {
    --canvas-bg: #faf7ec;
    --bordeaux: #520c2c;
    --gold: #c9a227;
    --cream: #f7ecd4;
    --white: #ffffff;
    --script: "Playball", cursive;
    --sans: "Raleway", "Helvetica Neue", Arial, sans-serif;
  }
  * { box-sizing: border-box; margin: 0; padding: 0; }
  html, body { width: 1200px; height: 690px; overflow: hidden; background: var(--canvas-bg); }
  .canvas { position: relative; width: 1200px; height: 690px; }

  /* Front of the card */
  .card-front {
    position: absolute; left: 335px; top: 30px;
    width: 240px; height: 437px;
    background: var(--bordeaux);
    box-shadow: 0 2px 6px rgba(0,0,0,.12);
    overflow: hidden;
  }
  .brand-name {
    position: absolute; left: 16px; right: 16px; top: 178px;
    text-align: center;
    font-family: var(--sans); font-weight: 600; font-size: 15px; line-height: 22px;
    letter-spacing: .04em;
    color: var(--white);
  }
  .website {
    position: absolute; left: 0; right: 0; bottom: 36px;
    text-align: center;
    font-family: var(--sans); font-weight: 600; font-size: 13px; color: var(--gold);
  }
  .gold-band {
    position: absolute; left: 0; right: 0; bottom: 3px; height: 11px;
    background: var(--gold);
  }

  /* Back of the card */
  .card-back {
    position: absolute; left: 581px; top: 242px;
    width: 284px; height: 434px;
    box-shadow: 0 2px 6px rgba(0,0,0,.12);
    overflow: hidden;
  }
  .back-message {
    position: absolute; left: 0; top: 0; width: 100%; height: 256px;
    background: var(--cream);
  }
  .rule {
    position: absolute; left: 12px; top: 32px; width: 200px; height: 3px;
    background: var(--gold);
  }
  .rule-mark {
    position: absolute; left: 222px; top: 27px; width: 13px; height: 13px;
    border-radius: 50%; background: var(--bordeaux);
  }
  .motto {
    position: absolute; right: 24px; top: 92px;
    text-align: right;
    font-family: var(--script); font-size: 19px; line-height: 26px;
    color: var(--bordeaux);
  }
  .back-contact {
    position: absolute; left: 0; top: 256px; width: 100%; height: 178px;
    background: var(--bordeaux);
    color: var(--white);
    font-family: var(--sans); font-size: 14px; line-height: 18px;
  }
  .contact-list { position: absolute; left: 25px; top: 84px; list-style: none; }
  .contact-name { font-weight: 600; }
  .back-contact .gold-band { bottom: 0; height: 10px; }
</style>
</head>
<body>
<main class="canvas">

  <section class="card-front" aria-label="Vorderseite der Visitenkarte">
    <p class="brand-name">Lichtfeder –<br>Zeilen von Hand zu Hand</p>
    <div class="website">www.helenabrandt.de</div>
    <div class="gold-band"></div>
  </section>

  <section class="card-back" aria-label="Rückseite der Visitenkarte">
    <div class="back-message">
      <div class="rule"></div>
      <div class="rule-mark"></div>
      <p class="motto">Mein Anliegen ist es,<br>Sie zu begeistern,<br>damit Sie Begeisterung<br>über Sich selbst<br>erkennen und erfahren.</p>
    </div>
    <div class="back-contact">
      <ul class="contact-list">
        <li class="contact-name">Helena Brandt</li>
        <li>lichtfeder@mailpost.de</li>
        <li>+49 160 55 214 907</li>
      </ul>
      <div class="gold-band"></div>
    </div>
  </section>

</main>
</body>
</html>
```